Courier Business needs a Business Card Design !!!

My new company needs a business card design. Our company name is Maple Dart Courier & Delivery Services. We will be servicing residential , government and business clients in the City of Yellowknife, Northwest Territories, Canada. I would like the following information included on the card: Name- Calvin Oxley. Title- Owner. Company- Maple Dart Courier & Delivery Services. Address- PO Box 5918 , Yellowknife , NWT, X0E 4K3. Phone- 867-555-0193. Email- mapledartdelivery@postfern.example. Facebook- www.socialpage.example/mapledartdelivery. I would like my double sided card to be the standard size of 84mm x 55mm. No borders. Use CMYK mode.1039x 697 pixels at least. I would like my logo to take up at least one quarter of the area of one side of the card. Text should be at least 8 point with perhaps my name being 10 point and my company name being 12-15 point . It should have clear readable font. Please use one or two bold colors. I am trying to attract the business community so a professional look might be best. My tag line is " On Time Every Time ". Nice safe margins please. We will be providing fast, reliable and professional delivery of envelopes and small packages within the City of Yellowknife. We offer 100% satisfaction or a complete refund. I have included a file of our logo. I like black, blue and red but am willing to look at what you feel would work best. I do not really like white as a background color.

Target Market(s)

Professionals , business owners. 30-50 years old

Industry/Entity Type

Residential

Contact Information for Business Card

As noted in brief

Font styles to use
Serif
Sans Serif

Colors
000000
0255a3
f04a50

Requirements
Must have
• My contact info. My logo
Nice to have
• Simple elegant design but still catches the eye
Should not have
• White background color

```html
<!DOCTYPE html>
<html lang="en">
<head>
<meta charset="utf-8">
<title>Maple Dart Courier &amp; Delivery Services – Business Card</title>
<link rel="stylesheet" href="https://fonts.googleapis.com/css2?family=Jost:wght@500;600;700&display=swap">
<style>
  :root {
    --pink: #f24a7e;
    --lime: #86e83b;
    --lime-deep: #5fb81e;
    --frame-red: #f2353f;
    --card-tint: #fdecf2;
    --white: #ffffff;
    --page: #ffffff;
  }
  html, body {
    margin: 0;
    padding: 0;
    width: 1200px;
    height: 1200px;
    overflow: hidden;
    background: var(--page);
  }
  .stage {
    position: relative;
    width: 1500px;
    height: 1500px;
    transform: scale(0.8);
    transform-origin: 0 0;
    font-family: "Jost", "Century Gothic", sans-serif;
  }
  .card {
    position: absolute;
    left: 232px;
    top: 467px;
    width: 1053px;
    height: 603px;
    box-sizing: border-box;
    border: 3px solid var(--frame-red);
    background: var(--card-tint);
    overflow: hidden;
  }
  .card-shapes {
    position: absolute;
    left: 0;
    top: 0;
    width: 1053px;
    height: 603px;
  }
  .brand {
    position: absolute;
    left: 230px;
    width: 700px;
    top: 58px;
    display: flex;
    justify-content: center;
    align-items: center;
    gap: 22px;
    color: var(--pink);
    font-weight: 700;
    line-height: 1;
  }
  .brand-mark {
    flex: none;
    width: 52px;
    height: 52px;
    border-radius: 50%;
    background: var(--pink);
  }
  .brand-text { text-align: center; }
  .brand-name {
    display: block;
    font-size: 60px;
    letter-spacing: 1px;
    text-transform: uppercase;
  }
  .brand-sub {
    display: block;
    margin-top: 8px;
    font-size: 27px;
    text-transform: uppercase;
    letter-spacing: 0.5px;
  }
  .tagline {
    position: absolute;
    left: 0;
    right: 0;
    top: 178px;
    padding-left: 45px;
    text-align: center;
    color: var(--lime-deep);
    font-size: 17px;
    font-weight: 600;
    letter-spacing: 6px;
    text-transform: uppercase;
  }
  .holder-name {
    position: absolute;
    left: 0;
    right: 0;
    top: 226px;
    padding-left: 45px;
    text-align: center;
    color: var(--pink);
    font-size: 38px;
    font-weight: 600;
  }
  .holder-title {
    position: absolute;
    left: 0;
    right: 0;
    top: 278px;
    padding-left: 45px;
    text-align: center;
    color: var(--pink);
    font-size: 24px;
    font-weight: 500;
    letter-spacing: 2px;
  }
  .holder-address {
    position: absolute;
    left: 0;
    right: 0;
    top: 330px;
    padding-left: 56px;
    text-align: center;
    color: var(--lime-deep);
    font-size: 30px;
    font-weight: 600;
  }
  .contact-list {
    position: absolute;
    left: 92px;
    top: 446px;
    margin: 0;
    padding: 0;
    list-style: none;
    color: var(--white);
    font-size: 28px;
    font-weight: 600;
  }
  .contact-item {
    display: flex;
    align-items: center;
    height: 36px;
  }
  .contact-icon {
    width: 36px;
    margin-right: 28px;
    display: flex;
    justify-content: center;
  }
  .contact-letter { font-size: 26px; }
</style>
</head>
<body>
<div class="stage">
  <section class="card">
    <svg class="card-shapes" viewBox="0 0 1053 603" aria-hidden="true">
      <polygon fill="var(--pink)" points="0,0 95,0 198,236 98,435 0,435 0,425 110,222 0,18"/>
      <rect fill="var(--pink)" x="0" y="435" width="1053" height="168"/>
    </svg>

    <div class="brand">
      <span class="brand-mark"></span>
      <span class="brand-text">
        <span class="brand-name">Maple Dart</span>
        <span class="brand-sub">Courier &amp; Delivery Services</span>
      </span>
    </div>
    <div class="tagline">On Time Every Time</div>

    <div class="holder-name">Calvin Oxley.</div>
    <div class="holder-title">OWNER</div>
    <div class="holder-address">PO Box 5918 , Yellowknife , NWT, X0E 4K3</div>

    <ul class="contact-list">
      <li class="contact-item">
        <span class="contact-icon">
          <svg width="18" height="28" viewBox="0 0 20 32" aria-hidden="true">
            <path fill="var(--white)" d="M14 2 C6 2 3 10 3 16 C3 22 6 30 14 30 L16 24 L12 22 C10 20 10 12 12 10 L16 8 Z"/>
          </svg>
        </span>
        867-555-0193
      </li>
      <li class="contact-item">
        <span class="contact-icon contact-letter">T.</span>
        Maple Dart Courier &amp; Delivery Services
      </li>
      <li class="contact-item">
        <span class="contact-icon">
          <svg width="30" height="20" viewBox="0 0 32 22" aria-hidden="true">
            <path fill="var(--white)" d="M0 2 L16 12 L32 2 L32 22 L0 22 Z"/>
            <path fill="var(--white)" d="M0 0 L32 0 L16 9 Z"/>
          </svg>
        </span>
        mapledartdelivery@postfern.example
      </li>
      <li class="contact-item">
        <span class="contact-icon">
          <svg width="26" height="26" viewBox="0 0 26 26" aria-hidden="true">
            <g fill="none" stroke="var(--white)" stroke-width="2.2">
              <circle cx="13" cy="13" r="11"/>
              <ellipse cx="13" cy="13" rx="5" ry="11"/>
              <line x1="2" y1="13" x2="24" y2="13"/>
            </g>
          </svg>
        </span>
        www.socialpage.example/mapledartdelivery
      </li>
    </ul>
  </section>
</div>
</body>
</html>
```